Velmor Integrated Company Profile

We are looking for a new design for our company profile. We need two output formats. A PDF version to use as a soft copy. Another version is needed for printing.

We are seeking an A4 profile based on the same text content of our old one. Some new content will be provided once the graphics are confirmed.

Attached is our old profile. Please give us a newer design. Once design is confirmed we will provide the new content to use.
I am available for any answers or feedback.

Target Market(s)

This is used for introducing our company to the customers.
We are also seeking investors, so they might be considered

Industry/Entity Type

Information Technology

Requirements
Must have
• Info-graphics based on the data in old profile
• Some info-graphics about number of orders, customers and sales volume
• We have two websites for selling online; nilecallstock.com and dunelinkdepot.com. We need to include them in a way or another in the profile. Their logos are in the attached files.
Nice to have
• Any new suggestions about content to include in the profile will be welcomed

```html
<!DOCTYPE html>
<html lang="en">
<head>
<meta charset="utf-8">
<title>Velmor Integrated – Strategy &amp; Values</title>
<link href="https://fonts.googleapis.com/css2?family=Russo+One&family=Ubuntu:wght@400;500&display=swap" rel="stylesheet">
<style>
  :root {
    --backdrop: #808080;
    --paper: #ffffff;
    --navy: #1d4a7a;
    --gold: #fcc332;
    --gold-pale: #fed999;
    --steel: #9fb3c8;
    --ink: #1a1a1a;
    --ink-soft: #444444;
    --ring: #ececec;
  }
  html, body {
    margin: 0;
    padding: 0;
    width: 1000px;
    height: 1200px;
    overflow: hidden;
    background: var(--backdrop);
  }
  .canvas {
    position: relative;
    width: 1000px;
    height: 1200px;
    background: var(--backdrop);
    font-family: "Ubuntu", sans-serif;
  }
  .page {
    position: absolute;
    left: 112px;
    top: 48px;
    width: 778px;
    height: 1100px;
    background: var(--paper);
    overflow: hidden;
  }
  .page > * { position: absolute; }
  .rings { left: 0; top: 0; }
  .corner-frames { left: 0; top: 0; }
  .hands-photo {
    left: 503px;
    top: 250px;
    width: 275px;
    height: 725px;
    background: linear-gradient(180deg, rgba(230,230,232,0) 0%, rgba(222,222,226,0.85) 20%, rgba(210,206,214,0.9) 50%, rgba(222,222,226,0.85) 80%, rgba(230,230,232,0) 100%);
  }
  .brand {
    left: 35px;
    top: 47px;
    display: flex;
    align-items: center;
    gap: 12px;
  }
  .brand-mark {
    width: 34px;
    height: 34px;
    background: var(--gold);
  }
  .brand-name {
    font-family: "Ubuntu", sans-serif;
    font-weight: 500;
    font-size: 26px;
    letter-spacing: 3px;
    color: var(--navy);
    text-transform: uppercase;
  }
  .section-title {
    font-family: "Russo One", sans-serif;
    color: var(--navy);
    font-size: 44px;
    margin: 0;
    letter-spacing: 0.5px;
    white-space: nowrap;
  }
  .strategy-title { left: 108px; top: 210px; }
  .values-title { left: 158px; top: 690px; }
  .step { left: 88px; display: flex; }
  .step-number {
    width: 94px;
    height: 94px;
    border-radius: 50%;
    background: var(--navy);
    color: var(--paper);
    font-family: "Russo One", sans-serif;
    font-size: 56px;
    display: flex;
    align-items: center;
    justify-content: center;
    flex: none;
  }
  .step-body { margin-left: 42px; margin-top: -2px; }
  .step-heading {
    margin: 0 0 2px;
    font-weight: 400;
    font-size: 27px;
    color: var(--navy);
  }
  .step-list {
    margin: 0;
    padding: 0 0 0 37px;
    font-size: 16px;
    line-height: 21.5px;
    color: var(--ink);
  }
  .step-1 { top: 297px; }
  .step-2 { top: 424px; }
  .step-3 { top: 555px; }
  .step-3 .step-body { margin-left: 45px; }
  .value-card {
    top: 772px;
    width: 173px;
    height: 180px;
    border-radius: 8px;
    background: var(--gold);
    color: var(--ink-soft);
    font-size: 14px;
    line-height: 18.6px;
    text-align: center;
    display: flex;
    align-items: center;
    justify-content: center;
    padding: 0 12px;
    box-sizing: border-box;
  }
  .value-card p { margin: 0; }
  .value-commitment { left: 38px; }
  .value-expediency { left: 246px; align-items: flex-start; padding-top: 16px; }
  .value-ingenuity { left: 460px; align-items: flex-start; padding-top: 32px; }
  .tagline-band {
    left: 468px;
    top: 974px;
    width: 310px;
    height: 126px;
    background: var(--navy);
    color: var(--paper);
    box-sizing: border-box;
    padding: 12px 0 0 35px;
    line-height: 1;
  }
  .tagline-lead { display: block; font-size: 40px; }
  .tagline-rest { display: block; font-size: 24px; margin-top: 3px; line-height: 24px; }
</style>
</head>
<body>
<div class="canvas">
  <main class="page">
    <svg class="rings" width="778" height="1100" viewBox="0 0 778 1100" aria-hidden="true">
      <g fill="none" stroke="var(--ring)" stroke-width="2">
        <circle cx="335" cy="560" r="200"/>
        <circle cx="335" cy="560" r="300"/>
        <circle cx="335" cy="560" r="410"/>
        <circle cx="335" cy="560" r="520"/>
      </g>
    </svg>

    <div class="hands-photo" role="img" aria-label="Two hands joining a pair of puzzle pieces, black and white photograph"></div>

    <svg class="corner-frames" width="778" height="1100" viewBox="0 0 778 1100" aria-hidden="true">
      <path d="M498 42 H778 V272 H498 Z M543 44 V224 H723 V44 Z" fill="var(--steel)" fill-rule="evenodd" opacity="0.9"/>
      <path d="M378 0 H768 V384 H723 V42 H378 Z" fill="var(--gold-pale)" opacity="0.9"/>
    </svg>

    <div class="brand">
      <span class="brand-mark"></span>
      <span class="brand-name">Velmor Integrated</span>
    </div>

    <h1 class="section-title strategy-title">OUR STRATEGY</h1>

    <section class="step step-1">
      <div class="step-number">1</div>
      <div class="step-body">
        <h2 class="step-heading">Assess &amp; Design</h2>
        <ul class="step-list">
          <li>Business &amp; Technical Assessment.</li>
          <li>Client’s objective.</li>
          <li>Solution Design &amp; TCO analysis.</li>
        </ul>
      </div>
    </section>

    <section class="step step-2">
      <div class="step-number">2</div>
      <div class="step-body">
        <h2 class="step-heading">Implement</h2>
        <ul class="step-list">
          <li>Project plan &amp; management.</li>
          <li>Certified technical team.</li>
          <li>Quality Assurance.</li>
          <li>Documentation &amp; training.</li>
        </ul>
      </div>
    </section>

    <section class="step step-3">
      <div class="step-number">3</div>
      <div class="step-body">
        <h2 class="step-heading">Follow up</h2>
        <ul class="step-list">
          <li>ROI and adoption assurance.</li>
          <li>Budget flexible service plans.</li>
          <li>Upgrades and fixes communication</li>
        </ul>
      </div>
    </section>

    <h1 class="section-title values-title">OUR VALUES</h1>

    <div class="value-card value-commitment"><p>Commitment For those who are committed, a promise is a responsibility, and this is how we guarantee a superior service</p></div>
    <div class="value-card value-expediency"><p>Expediency Accurately and professionally providing the most suitable solution for your needs and perfectly apply it</p></div>
    <div class="value-card value-ingenuity"><p>Ingenuity Innovating creative techniques for our services and products</p></div>

    <div class="tagline-band">
      <span class="tagline-lead">THE HOUSE</span>
      <span class="tagline-rest">OF UNIFIED<br>COMMUNICATION</span>
    </div>
  </main>
</div>
</body>
</html>
```